Nursing Concepts Diagram

We are looking to make a diagram to represent the Conceptual Framework of our nursing program (college). The frame work is based on three parts:

I. Nursing Process

II. Core Concepts
a. Clinical Competence
b. Critical Thinking
c. Moral/Ethical Principles
d. Growth Mindset
e. Caring/Compassion
f. Cultural Competence
g. Effective Communication
h. Life-long Learning

III. Tervane's Hierarchy of Needs

I have attached two sketches to give you a sense of how I think this could work.

Please also consider the following:

-Tervane's Hierarchy of Needs is always represented in the shape of a pyramid so I think the other two components (Nursing Process and Core Concepts) should complement that.

Target Market(s)

Healthcare Professionals, Nursing Educators

Font styles to use
Sans Serif

Colors

Designer to choose colors to be used in the design.

Requirements
Must have
• We would like the diagram to include a legend somewhere on the paper that outlines the parts of each component like demonstrated in the attached table
• All the small parts of the Nursing Process and Tervane's Hierarchy of Needs don't need to be listed out in the diagram because it may look too wordy, but the eight parts that make up the core concepts should all be listed
• The Nursing Process and Tervane's Hierachy of needs should both border each of the 8 core concepts so that it can show a relation.

```html
<!DOCTYPE html>
<html lang="en">
<head>
<meta charset="utf-8">
<title>Nursing Concepts Framework</title>
<link href="https://fonts.googleapis.com/css2?family=Arimo&family=Tinos&family=Jura:wght@500&display=swap" rel="stylesheet">
<style>
  :root {
    --page: #ffffff;
    --ink: #111111;
    --blue-light: #12b0ec;
    --blue-dark: #1a6fb8;
    --grey-light: #f6f6f6;
    --grey-mid: #d4d4d4;
    --grey-dark: #a9a9a9;
    --rule: #ffffff;
  }
  html, body {
    margin: 0;
    padding: 0;
    width: 1200px;
    height: 848px;
    overflow: hidden;
    background: var(--page);
  }
  .framework {
    display: block;
    width: 1200px;
    height: 848px;
  }
  .title {
    font-family: "Tinos", "Times New Roman", serif;
    font-size: 52px;
    fill: var(--ink);
  }
  .concept {
    font-family: "Arimo", Arial, sans-serif;
    font-size: 19px;
    fill: var(--ink);
  }
  .pyramid-label {
    font-family: "Jura", sans-serif;
    font-weight: 500;
    font-size: 25px;
    fill: var(--ink);
  }
  .divider {
    stroke: var(--rule);
    stroke-width: 2;
  }
</style>
</head>
<body>
<svg class="framework" viewBox="0 0 1200 848" xmlns="http://www.w3.org/2000/svg" aria-label="Nursing program conceptual framework">
  <defs>
    <linearGradient id="domeFill" x1="0" y1="0" x2="0" y2="1">
      <stop offset="0" stop-color="#e4e4e4"/>
      <stop offset="1" stop-color="#bdbdbd"/>
    </linearGradient>
    <linearGradient id="bodyFill" x1="0" y1="0" x2="1" y2="0">
      <stop offset="0" stop-color="var(--grey-dark)"/>
      <stop offset="0.25" stop-color="var(--grey-mid)"/>
      <stop offset="0.5" stop-color="var(--grey-light)"/>
      <stop offset="0.75" stop-color="var(--grey-mid)"/>
      <stop offset="1" stop-color="var(--grey-dark)"/>
    </linearGradient>
    <linearGradient id="bandFill" x1="0" y1="0" x2="1" y2="0">
      <stop offset="0" stop-color="var(--blue-dark)"/>
      <stop offset="0.5" stop-color="var(--blue-light)"/>
      <stop offset="1" stop-color="var(--blue-dark)"/>
    </linearGradient>
    <linearGradient id="pyramidFill" x1="0" y1="0" x2="0" y2="1">
      <stop offset="0" stop-color="var(--blue-light)"/>
      <stop offset="1" stop-color="#1589d0"/>
    </linearGradient>
    <radialGradient id="floorShadow" cx="0.5" cy="0.5" r="0.5">
      <stop offset="0" stop-color="#000" stop-opacity="0.35"/>
      <stop offset="1" stop-color="#000" stop-opacity="0"/>
    </radialGradient>
    <radialGradient id="figureFill" cx="0.5" cy="0.4" r="0.6">
      <stop offset="0" stop-color="#f2e4da"/>
      <stop offset="1" stop-color="#ffffff" stop-opacity="0"/>
    </radialGradient>
  </defs>

  <ellipse class="floor-shadow" cx="600" cy="652" rx="340" ry="40" fill="url(#floorShadow)"/>

  <path class="cap-dome" d="M338,345 C342,262 380,240 600,237 C820,240 858,262 862,345 Z" fill="url(#domeFill)"/>
  <text class="title" x="600" y="302" text-anchor="middle">Nursing Process</text>

  <path class="cap-body" d="M207,405 Q600,285 993,405 L848,638 L352,638 Z" fill="url(#bodyFill)"/>
  <path class="cap-band" d="M197,372 Q600,258 1003,372 L993,405 Q600,285 207,405 Z" fill="url(#bandFill)"/>

  <g class="nurse-figure" role="img" aria-label="Illustration of a nurse wearing a white cap and uniform">
    <rect x="552" y="318" width="96" height="128" rx="30" fill="url(#figureFill)"/>
  </g>

  <g class="core-concepts-left">
    <text class="concept" x="405" y="422" text-anchor="middle">Clinical Competence</text>
    <line class="divider" x1="307" y1="441" x2="495" y2="441"/>
    <text class="concept" x="399" y="471" text-anchor="middle">Critical Thinking</text>
    <line class="divider" x1="323" y1="492" x2="478" y2="492"/>
    <text class="concept" x="401" y="532" text-anchor="middle">Growth Mindset</text>
    <line class="divider" x1="323" y1="553" x2="478" y2="553"/>
    <text class="concept" x="398" y="581" text-anchor="middle">Moral/Ethical</text>
    <text class="concept" x="398" y="603" text-anchor="middle">Principles</text>
  </g>

  <g class="core-concepts-right">
    <text class="concept" x="809" y="422" text-anchor="middle">Cultural Competence</text>
    <line class="divider" x1="707" y1="441" x2="896" y2="441"/>
    <text class="concept" x="806" y="471" text-anchor="middle">Caring/Compassion</text>
    <line class="divider" x1="725" y1="492" x2="878" y2="492"/>
    <text class="concept" x="804" y="522" text-anchor="middle">Effective</text>
    <text class="concept" x="806" y="543" text-anchor="middle">Communication</text>
    <line class="divider" x1="725" y1="553" x2="878" y2="553"/>
    <text class="concept" x="802" y="582" text-anchor="middle">Life-long</text>
    <text class="concept" x="803" y="603" text-anchor="middle">Learning</text>
  </g>

  <g class="hierarchy-pyramid">
    <polygon points="600,434 463,607 736,607" fill="url(#pyramidFill)"/>
    <text class="pyramid-label" x="600" y="523" text-anchor="middle">Tervane's</text>
    <text class="pyramid-label" x="600" y="558" text-anchor="middle">Hierarchy</text>
    <text class="pyramid-label" x="600" y="593" text-anchor="middle">of Needs</text>
  </g>
</svg>
</body>
</html>
```